Business Card Design Project : Tidewell Press

In preparation for market launch, Whistler's Tidewell Press require the development of a business card. Tidewell Press is a Community online publishing web portal. We provide the the city of Whistler located in B.C. (Canada) business directories, News, Classified ads, News, Events and blogs etc.

The main focus of the brand is to help local businesses to corporate with their online advertisement and marketing. Meeting our clients face to face is a must (B2B).

Target Market(s)

The target market is B2B customers. Business Owners to Marketing, advertising Managers

Industry/Entity Type

Business

Requirements
Must have
• - The business card will be two sided.
the BACK side will have our logo which consist of (icon, url,slogan) submited. The logo will be middle and centred.

The FRONT side should have company details:

Company Legal Name: FERNDALE TIDEWELL PRESS

Owen Marsk
Director of Sales & Marketing

www.ferndaletidewell.biz
owen@ferndaletidewell.biz

Phone: 555 014 3826
#2817 - 562 E. Harlow Ave.
Vancouver, B.C. K7P2R4 Canada
Nice to have
• - For the "FRONT" side of our business card. You can separate or re-arrange with our logo components (icon, logo,slogan). It does not have to be together.

Also our company legal name is rather long so arrange or organize the name in a way to make it shorter. Your experience and creativity will have to come in play.
Should not have
• should not have other colors beside logo color and black text (2 colors). Also nothing Three dimensional

```html
<!DOCTYPE html>
<html lang="en">
<head>
<meta charset="utf-8">
<title>Tidewell Press — Business Card</title>
<link rel="stylesheet" href="https://fonts.googleapis.com/css2?family=Source+Sans+3:wght@400;600;700&display=swap">
<style>
  :root {
    --brand-blue: #2b74b9;
    --ink: #111418;
    --paper: #f4f5f7;
    --mist: #dde3ea;
    --backdrop: #e9e6e1;
  }
  * { box-sizing: border-box; margin: 0; padding: 0; }
  html, body {
    width: 1200px; height: 880px; overflow: hidden;
    background: var(--backdrop);
    font-family: "Source Sans 3", "Myriad Pro", Arial, sans-serif;
    color: var(--ink);
  }
  .canvas {
    width: 1200px; height: 880px;
    display: flex; flex-direction: column; align-items: center; justify-content: center;
    gap: 40px;
  }
  .card {
    position: relative; width: 680px; height: 389px; overflow: hidden;
    box-shadow: 0 2px 6px rgba(0,0,0,0.18);
  }

  /* Front side */
  .card--front { background: var(--paper); }
  .card__swoosh { position: absolute; inset: 0; width: 100%; height: 100%; }
  .brand-block { position: absolute; left: 40px; top: 58px; }
  .brand-name {
    display: flex; align-items: center; gap: 10px;
    font-size: 24px; font-weight: 700; color: var(--brand-blue); margin-bottom: 6px;
  }
  .brand-dot { width: 18px; height: 18px; border-radius: 50%; background: var(--brand-blue); }
  .brand-url { font-size: 22px; font-weight: 700; color: var(--ink); letter-spacing: -0.3px; line-height: 1; }
  .brand-slogan { font-size: 16px; color: var(--brand-blue); margin-top: 2px; }
  .company { position: absolute; left: 40px; top: 190px; font-size: 14.5px; line-height: 1.45; }
  .company__name { font-weight: 700; font-size: 14px; letter-spacing: 0.2px; }
  .person { position: absolute; left: 330px; top: 238px; font-size: 14.5px; line-height: 1.4; }
  .person__name { font-size: 20px; font-weight: 700; color: var(--brand-blue); }
  .person__rule { width: 220px; height: 1px; background: var(--ink); margin: 10px 0 8px; }

  /* Back side */
  .card--back {
    background: var(--brand-blue);
    display: flex; flex-direction: column; align-items: center; justify-content: center;
    text-align: center;
  }
  .back-name {
    display: flex; align-items: center; gap: 14px;
    font-size: 46px; font-weight: 700; color: var(--mist); margin-bottom: 14px;
  }
  .back-name .brand-dot { width: 30px; height: 30px; background: var(--mist); }
  .back-url { font-size: 40px; font-weight: 700; color: var(--ink); letter-spacing: -0.5px; line-height: 1; }
  .back-slogan { font-size: 27px; color: var(--mist); margin-top: 4px; }
</style>
</head>
<body>
<main class="canvas">

  <section class="card card--front" aria-label="Business card front">
    <svg class="card__swoosh" viewBox="0 0 680 389" preserveAspectRatio="none" aria-hidden="true">
      <path d="M0,0 H680 V389 H575 C625,250 585,95 445,48 C330,14 150,16 0,16 Z" fill="var(--brand-blue)"/>
      <path d="M452,52 C590,100 618,250 560,389 H545 C598,255 570,110 452,52 Z" fill="var(--ink)"/>
      <path d="M545,389 C598,255 570,110 452,52 C578,120 592,255 540,389 Z" fill="var(--paper)"/>
    </svg>

    <div class="brand-block">
      <div class="brand-name"><span class="brand-dot"></span>Tidewell Press</div>
      <div class="brand-url">www.ferndaletidewell.biz</div>
      <div class="brand-slogan">Your information gateway</div>
    </div>

    <address class="company" style="font-style:normal">
      <div class="company__name">FERNDALE TIDEWELL PRESS</div>
      <div>#2817 - 562 E. Harlow Ave.</div>
      <div>Vancouver, B.C. K7P2R4 Canada</div>
      <div>Phone: 555 014 3826</div>
    </address>

    <div class="person">
      <div class="person__name">Owen Marsk</div>
      <div class="person__title">Director of Sales &amp; Marketing</div>
      <div class="person__rule"></div>
      <div>www.ferndaletidewell.biz</div>
      <div>owen@ferndaletidewell.biz</div>
    </div>
  </section>

  <section class="card card--back" aria-label="Business card back">
    <div class="back-name"><span class="brand-dot"></span>Tidewell Press</div>
    <div class="back-url">www.ferndaletidewell.biz</div>
    <div class="back-slogan">Your information gateway</div>
  </section>

</main>
</body>
</html>
```